Business Card Design

Lawyer
Business name "HarlowLaw"
Areas of expertise:
property
commercial
trusts
immigration
franchising
I want the following quote on the back of the card somewhere.
"Education is when you read the fine print,
experience is what you get if you don't." Miles Corbell
Probably the "areas of expertise" should be on the back also to avoid cluttering the front.
As for colours, I like the shades of blue used on qerivo.com.
The basic part of the card with the contact info needs to be white and uncluttered.
Target Market(s)
small to medium sized self employed business people
Industry/Entity Type
Business
Contact Information for Business Card
Dennis Harlow
Phone + 64 9 517 4460
Fax: + 64 9 517 4461
PO Box 742
Clevedon
Auckland 2248
NZ
email: dennis@pinecrestlegal.co.nz

```html
<!DOCTYPE html>
<html lang="en">
<head>
<meta charset="utf-8">
<title>HarlowLaw – Business Card Back</title>
<link rel="stylesheet" href="https://fonts.googleapis.com/css2?family=Arimo:wght@700&display=swap">
<style>
  :root {
    --page: #ffffff;
    --blue-glow: #00aeef;
    --blue-mid: #0096dc;
    --blue-edge: #0072bc;
    --blue-shade: #005fa8;
    --ink: #0d0d0d;
  }
  html, body {
    margin: 0;
    padding: 0;
    width: 1200px;
    height: 741px;
    overflow: hidden;
    background: var(--page);
  }
  .card-back {
    position: relative;
    width: 1200px;
    height: 741px;
    border-radius: 34px;
    overflow: hidden;
    background: radial-gradient(ellipse 760px 560px at 585px 285px,
                var(--blue-glow) 0%, var(--blue-mid) 45%, var(--blue-edge) 100%);
  }
  .card-back__sweep {
    position: absolute;
    inset: 0;
    width: 100%;
    height: 100%;
  }
  .quote {
    position: absolute;
    left: 240px;
    top: 327px;
    width: 722px;
    margin: 0;
    font-family: "Arimo", Arial, sans-serif;
    font-weight: 700;
    color: var(--ink);
  }
  .quote__text {
    margin: 0;
    font-size: 34.5px;
    line-height: 41px;
    text-align: center;
  }
  .quote__author {
    display: block;
    padding-right: 9px;
    font-size: 34.5px;
    line-height: 41px;
    font-style: normal;
    text-align: right;
  }
</style>
</head>
<body>
  <section class="card-back">
    <svg class="card-back__sweep" viewBox="0 0 1200 741" aria-hidden="true">
      <path d="M0,40 C110,380 560,640 1200,741 L0,741 Z" fill="var(--blue-shade)" opacity="0.18"/>
      <path d="M0,130 C140,430 560,660 1110,741 L0,741 Z" fill="var(--blue-shade)" opacity="0.22"/>
    </svg>
    <figure class="quote">
      <blockquote class="quote__text">"Education is when you read the fine print,<br>experience is what you get if you don't."</blockquote>
      <cite class="quote__author">Miles Corbell</cite>
    </figure>
  </section>
</body>
</html>
```